PowerPoint Strategy presentation to be converted to professional looking

Convert the supplied PowerPoint presentation to a professional strategy presentation. Designer must have knowledge of how strategies are presented.

Target Market(s)

Management team

Industry/Entity Type

Finance

Font styles to use
Sans Serif

Colors
0054AA
0677BA
7BADD7
CADEEF
E8F1F8

Requirements
Must have
• Strategy must look professional
Nice to have
• Animations would be welcomed

```html
<!DOCTYPE html>
<html lang="en">
<head>
<meta charset="utf-8">
<title>EXCOM Alignment Transformation Strategy</title>
<link href="https://fonts.googleapis.com/css2?family=Poppins:wght@400;500;600;700&display=swap" rel="stylesheet">
<style>
:root{
  --primary:#0054AA;
  --accent:#0677BA;
  --soft:#7BADD7;
  --pale:#CADEEF;
  --mist:#E8F1F8;
  --ink:#1f2d3d;
  --muted:#4a5766;
  --line:#CADEEF;
  --white:#fff;
}
*{box-sizing:border-box;margin:0;padding:0}
html,body{width:1200px;height:4051px;overflow:hidden;background:var(--mist);font-family:"Poppins",sans-serif;color:var(--ink)}
.slide{position:absolute;left:75px;width:1048px;height:590px;background:var(--white);box-shadow:0 2px 14px rgba(0,84,170,.1);overflow:hidden}
.abs{position:absolute}
.heading{font-family:"Poppins",sans-serif;font-weight:600}
.brand{position:absolute;font-family:"Poppins",sans-serif;font-weight:600;color:var(--primary);font-size:15px;display:flex;align-items:center;gap:7px;white-space:nowrap}
.brand .dot{width:9px;height:9px;border-radius:50%;background:var(--primary)}
.header{position:absolute;left:0;top:0;width:1048px;height:100px}
.header-title{position:absolute;left:60px;top:29px;color:var(--white);font-size:26px;letter-spacing:.3px;line-height:34px;white-space:nowrap}
.footer-line{position:absolute;left:0;right:0;top:554px;height:1px;background:var(--line)}
.page-no{position:absolute;left:951px;top:547px;width:30px;height:30px;border-radius:50%;background:var(--primary);color:#fff;font-size:13px;font-weight:600;display:flex;align-items:center;justify-content:center}
/* cover */
.cover-title{position:absolute;left:61px;top:178px;font-size:31px;line-height:44px;color:var(--primary)}
.pill{position:absolute;left:61px;top:371px;width:225px;height:37px;border-radius:19px;background:var(--primary);color:#fff;font-size:13px;font-weight:500;display:flex;align-items:center;justify-content:center}
/* agenda */
.agenda-item{position:absolute;display:flex;align-items:center;gap:20px;font-size:19px;font-weight:500;color:var(--ink)}
.icon-disc{width:70px;height:70px;border-radius:50%;display:flex;align-items:center;justify-content:center;box-shadow:0 4px 10px rgba(0,84,170,.25);border:5px solid #fff;flex:none}
.icon-disc.dark{background:var(--primary)}
.icon-disc.alt{background:var(--accent)}
/* swot */
.swot-card{position:absolute;width:216px;height:275px;border:3px solid var(--primary);border-radius:3px;background:#fff;padding:64px 12px 0 12px}
.swot-card.alt{border-color:var(--accent)}
.swot-card h3{font-size:14px;font-weight:600;text-align:center;margin-bottom:10px;letter-spacing:.3px;color:var(--ink)}
.swot-card .badge{position:absolute;left:71px;top:-38px;width:68px;height:68px;border-radius:50%;background:var(--primary);border:4px solid #fff;display:flex;align-items:center;justify-content:center}
.swot-card.alt .badge{background:var(--accent)}
.list{list-style:none}
.list li{position:relative;padding-left:17px;font-size:10px;line-height:13px;margin-bottom:7px;color:var(--muted)}
.list li::before{content:"";position:absolute;left:2px;top:3px;width:5px;height:5px;border:2px solid var(--primary);border-radius:50%}
.swot-card.alt .list li::before,.list.alt li::before{border-color:var(--accent)}
/* statement */
.statement{position:absolute;left:60px;top:222px;width:390px;font-size:12px;line-height:23.5px;text-align:justify;color:var(--muted)}
.statement p+p{margin-top:12px}
/* pillars */
.pillar-icon{position:absolute;width:66px;height:66px;border-radius:50%;background:var(--accent);border:4px solid #fff;box-shadow:0 3px 10px rgba(6,119,186,.35);display:flex;align-items:center;justify-content:center}
.pillar-label{position:absolute;font-size:14px;font-weight:500;line-height:20px;color:var(--ink);letter-spacing:.2px;white-space:nowrap}
.blue-heading{position:absolute;left:0;width:1048px;text-align:center;color:var(--primary);font-size:20px;font-weight:500}
/* hr */
.hr-frame{position:absolute;top:190px;width:211px;height:211px;border:1.5px dashed var(--soft);padding:17px}
.hr-frame.solid{border:2px solid var(--primary)}
.hr-frame.accentdash{border-color:var(--accent)}
.hr-box{width:100%;height:100%;display:flex;flex-direction:column;align-items:center;justify-content:center;color:#fff;font-size:12px;font-weight:600;text-align:center;line-height:20px;gap:14px}
.hr-box.soft{background:var(--soft)}
.hr-box.dark{background:var(--primary)}
.hr-box.alt{background:var(--accent)}
.hr-list{position:absolute;top:427px;width:190px}
.hr-list li{font-size:9px;line-height:12px;margin-bottom:7px}
.hr-list li::before{width:4px;height:4px;top:2px}
.hr-list.soft li::before{border-color:var(--soft)}
</style>
</head>
<body>

<section class="slide" style="top:86px">
  <div class="brand" style="left:63px;top:26px"><span class="dot"></span>Noor Al Sakan</div>
  <svg class="abs" style="left:0;top:0" width="1048" height="590" viewBox="0 0 1048 590">
    <defs>
      <linearGradient id="coverPhoto" x1="0" y1="0" x2="1" y2="1">
        <stop offset="0" stop-color="#7BADD7"/>
        <stop offset=".5" stop-color="#CADEEF"/>
        <stop offset="1" stop-color="#0677BA"/>
      </linearGradient>
    </defs>
    <path d="M470 0 C 400 150 420 430 600 590 L 582 590 C 405 430 385 150 452 0 Z" fill="var(--primary)"/>
    <path d="M478 0 C 410 150 430 430 608 590 L1048 590 L1048 0 Z" fill="url(#coverPhoto)" role="img" aria-label="Photo of two colleagues reviewing charts on a laptop in front of a presentation screen"/>
  </svg>
  <h1 class="cover-title heading">EXCOM<br>ALIGNMENT<br>TRANSFORMATION<br>STRATEGY</h1>
  <div class="pill">NASTransformation 2026</div>
</section>

<section class="slide" style="top:744px">
  <svg class="header" viewBox="0 0 1048 100"><path d="M0 0 H872 C838 4 818 90 760 90 H0 Z" fill="var(--primary)"/><path d="M760 90 C820 90 842 10 880 2 C848 16 830 96 760 96 Z" fill="var(--soft)"/></svg>
  <h2 class="header-title heading">AGENDA</h2>
  <div class="brand" style="left:862px;top:36px"><span class="dot"></span>Noor Al Sakan</div>
  <svg class="abs" style="left:0;top:0" width="1048" height="590" viewBox="0 0 1048 590">
    <path d="M140 300 A178 178 0 0 1 470 250" fill="none" stroke="var(--accent)" stroke-width="5"/>
    <circle cx="318" cy="341" r="163" fill="#5b86ad" role="img" aria-label="Photo of hands using a calculator with tax and finance icons"/>
    <path d="M520 162 C600 200 610 300 589 332 C570 370 560 420 520 500" fill="none" stroke="var(--soft)" stroke-width="1.5" stroke-dasharray="3 4"/>
    <circle cx="520" cy="162" r="3" fill="var(--primary)"/><circle cx="520" cy="500" r="3" fill="var(--primary)"/>
  </svg>
  <div class="agenda-item" style="left:523px;top:177px"><span class="icon-disc dark"><svg width="28" height="28" viewBox="0 0 28 28" fill="none" stroke="#fff" stroke-width="2"><circle cx="12" cy="12" r="8"/><path d="M18 18 L25 25"/></svg></span>Current State Evaluation</div>
  <div class="agenda-item" style="left:554px;top:297px"><span class="icon-disc alt"><svg width="28" height="28" viewBox="0 0 28 28" fill="none" stroke="#fff" stroke-width="2"><path d="M4 24 V16 M11 24 V10 M18 24 V13 M25 24 V5"/></svg></span>Strategy and Financial Plan</div>
  <div class="agenda-item" style="left:523px;top:416px"><span class="icon-disc dark"><svg width="28" height="28" viewBox="0 0 28 28" fill="none" stroke="#fff" stroke-width="2"><circle cx="14" cy="11" r="7"/><path d="M10 20 H18 M11 24 H17"/></svg></span>Other Initiatives</div>
  <div class="footer-line"></div><div class="page-no">2</div>
</section>

<section class="slide" style="top:1401px">
  <svg class="header" viewBox="0 0 1048 100"><path d="M0 0 H872 C838 4 818 90 760 90 H0 Z" fill="var(--primary)"/><path d="M760 90 C820 90 842 10 880 2 C848 16 830 96 760 96 Z" fill="var(--soft)"/></svg>
  <h2 class="header-title heading">NAS SWOT ANALYSIS</h2>
  <div class="brand" style="left:862px;top:36px"><span class="dot"></span>Noor Al Sakan</div>
  <div class="swot-card" style="left:63px;top:192px">
    <span class="badge"><svg width="30" height="30" viewBox="0 0 30 30" fill="none" stroke="#fff" stroke-width="2"><rect x="5" y="6" width="20" height="18"/><path d="M9 12 H21 M9 17 H18"/></svg></span>
    <h3>STRENGTHS</h3>
    <ul class="list"><li>Mortgage specialization</li><li>Baytna program</li><li>NBFI market share</li><li>Program management expertise</li><li>Mortgage servicing capabilities</li><li>Off balance sheet loan book</li></ul>
  </div>
  <div class="swot-card alt" style="left:297px;top:230px">
    <span class="badge"><svg width="30" height="30" viewBox="0 0 30 30" fill="none" stroke="#fff" stroke-width="2"><path d="M5 25 V18 M12 25 V13 M19 25 V16 M26 25 V8"/></svg></span>
    <h3>WEAKNESSES</h3>
    <ul class="list"><li>Mortgage only</li><li>Ready-unit only</li><li>Baytna Program concentration</li><li>Geographical reach</li><li>Revenue stream dependency</li><li>On-balance Sheet portfolio size</li></ul>
  </div>
  <div class="swot-card" style="left:535px;top:192px">
    <span class="badge"><svg width="30" height="30" viewBox="0 0 30 30" fill="none" stroke="#fff" stroke-width="2"><rect x="6" y="10" width="18" height="15"/><path d="M15 3 V10 M11 7 L15 3 L19 7"/></svg></span>
    <h3>THREATS</h3>
    <ul class="list"><li>Baytna shift</li><li>HFDF shift</li><li>MHA shift</li><li>Speed of digital transformation</li><li>Regulatory oversight</li><li>Competitive pressure from banks</li><li>Macro factors (interest rates / property values)</li></ul>
  </div>
  <div class="swot-card alt" style="left:771px;top:230px">
    <span class="badge"><svg width="30" height="30" viewBox="0 0 30 30" fill="none" stroke="#fff" stroke-width="2"><path d="M4 26 H26 M8 26 V16 H14 V26 M16 26 V10 H22 V26"/></svg></span>
    <h3>OPPORTUNITIES</h3>
    <ul class="list"><li>Grow market share of existing products</li><li>Explore new markets</li><li>Develop new mortgage products</li><li>Digital innovation</li><li>Develop new business lines</li></ul>
  </div>
  <div class="footer-line"></div><div class="page-no">3</div>
</section>

<section class="slide" style="top:2059px">
  <svg class="header" viewBox="0 0 1048 100"><path d="M0 0 H872 C838 4 818 90 760 90 H0 Z" fill="var(--primary)"/><path d="M760 90 C820 90 842 10 880 2 C848 16 830 96 760 96 Z" fill="var(--soft)"/></svg>
  <h2 class="header-title heading">TRANSFORMATION STRATEGY STATEMENT</h2>
  <div class="brand" style="left:862px;top:36px"><span class="dot"></span>Noor Al Sakan</div>
  <div class="statement">
    <p>As we transform into a comprehensive financial services company, we remain committed to continue extending our range and reach of mortgage solutions.</p>
    <p>Our strategy involves expanding our offering beyond mortgages to deliver a broader range of financial solutions to consumers and small and medium enterprises while maintaining our commitment to bespoke experience and technological advancement.</p>
  </div>
  <div role="img" aria-label="Photo of business people working with a laptop, tablet and printed charts" style="position:absolute;left:528px;top:151px;width:458px;height:358px;border-radius:22px;border:5px solid #fff;box-shadow:0 4px 16px rgba(0,84,170,.2);background:linear-gradient(135deg,#CADEEF 0%,#7BADD7 45%,#0054AA 100%)"></div>
  <div class="footer-line"></div><div class="page-no">4</div>
</section>

<section class="slide" style="top:2716px">
  <svg class="header" viewBox="0 0 1048 100"><path d="M0 0 H872 C838 4 818 90 760 90 H0 Z" fill="var(--primary)"/><path d="M760 90 C820 90 842 10 880 2 C848 16 830 96 760 96 Z" fill="var(--soft)"/></svg>
  <h2 class="header-title heading">5 NAS TRANSFORMATION PILLARS</h2>
  <div class="brand" style="left:862px;top:36px"><span class="dot"></span>Noor Al Sakan</div>
  <svg class="abs" style="left:0;top:0" width="1048" height="590" viewBox="0 0 1048 590">
    <defs><filter id="softShadow" x="-20%" y="-20%" width="140%" height="140%"><feDropShadow dx="0" dy="3" stdDeviation="6" flood-color="#0054AA" flood-opacity=".18"/></filter></defs>
    <circle cx="525" cy="371" r="115" fill="none" stroke="var(--primary)" stroke-width="2.5"/>
    <circle cx="525" cy="371" r="90" fill="#fff" filter="url(#softShadow)"/>
    <g fill="none" stroke="var(--primary)" stroke-width="1.5">
      <path d="M525 256 V228"/><path d="M425 315 L395 283 H355"/><path d="M625 315 L655 283 H694"/><path d="M425 427 L395 459 H355"/><path d="M625 427 L655 459 H694"/>
    </g>
    <g fill="#fff" stroke="var(--primary)" stroke-width="2">
      <circle cx="525" cy="256" r="4"/><circle cx="425" cy="315" r="4"/><circle cx="625" cy="315" r="4"/><circle cx="425" cy="427" r="4"/><circle cx="625" cy="427" r="4"/>
    </g>
  </svg>
  <div class="brand" style="left:467px;top:359px"><span class="dot"></span>Noor Al Sakan</div>
  <div class="pillar-label" style="left:439px;top:122px">MARKET DEVELOPMENT</div>
  <div class="pillar-icon" style="left:492px;top:162px"><svg width="28" height="28" viewBox="0 0 28 28" fill="none" stroke="#fff" stroke-width="2"><path d="M3 25 H25 M7 25 V17 M13 25 V12 M19 25 V8"/></svg></div>
  <div class="pillar-label" style="left:161px;top:254px;text-align:right">PRODUCT<br>DEVELOPMENT</div>
  <div class="pillar-icon" style="left:288px;top:250px"><svg width="28" height="28" viewBox="0 0 28 28" fill="none" stroke="#fff" stroke-width="2"><circle cx="14" cy="14" r="6"/><circle cx="14" cy="14" r="11" stroke-dasharray="4 3"/></svg></div>
  <div class="pillar-label" style="left:787px;top:273px">DIVERSIFICATION</div>
  <div class="pillar-icon" style="left:694px;top:250px"><svg width="28" height="28" viewBox="0 0 28 28" fill="none" stroke="#fff" stroke-width="2"><circle cx="14" cy="14" r="4"/><path d="M14 3 V9 M14 19 V25 M3 14 H9 M19 14 H25"/></svg></div>
  <div class="pillar-label" style="left:107px;top:449px">MARKET PENETRATION</div>
  <div class="pillar-icon" style="left:288px;top:426px"><svg width="28" height="28" viewBox="0 0 28 28" fill="none" stroke="#fff" stroke-width="2"><path d="M4 24 L11 15 L16 19 L24 7 M18 7 H24 V13"/></svg></div>
  <div class="pillar-label" style="left:787px;top:449px">TECHNOLOGY</div>
  <div class="pillar-icon" style="left:694px;top:426px"><svg width="28" height="28" viewBox="0 0 28 28" fill="none" stroke="#fff" stroke-width="2"><rect x="8" y="8" width="12" height="12"/><path d="M11 3 V8 M17 3 V8 M11 20 V25 M17 20 V25 M3 11 H8 M3 17 H8 M20 11 H25 M20 17 H25"/></svg></div>
  <div class="blue-heading" style="top:514px">NAS Transformation Pillars</div>
  <div class="footer-line"></div><div class="page-no">5</div>
</section>

<section class="slide" style="top:3374px">
  <svg class="header" viewBox="0 0 1048 100"><path d="M0 0 H872 C838 4 818 90 760 90 H0 Z" fill="var(--primary)"/><path d="M760 90 C820 90 842 10 880 2 C848 16 830 96 760 96 Z" fill="var(--soft)"/></svg>
  <h2 class="header-title heading">CORPORATE HR INITIATIVES</h2>
  <div class="brand" style="left:862px;top:36px"><span class="dot"></span>Noor Al Sakan</div>
  <div class="blue-heading" style="top:134px">Corporate Initiatives</div>
  <svg class="abs" style="left:0;top:0" width="1048" height="590" viewBox="0 0 1048 590">
    <g stroke="var(--primary)" stroke-width="1.5" fill="var(--primary)">
      <path d="M379 295 H410"/><path d="M410 291 L417 295 L410 299 Z"/>
      <path d="M630 295 H661"/><path d="M661 291 L668 295 L661 299 Z"/>
    </g>
  </svg>
  <div class="hr-frame" style="left:168px"><div class="hr-box soft"><svg width="32" height="32" viewBox="0 0 32 32" fill="none" stroke="#fff" stroke-width="2"><rect x="4" y="6" width="22" height="16"/><circle cx="20" cy="20" r="6"/><path d="M24 24 L29 29"/></svg><span>NEW HR<br>STRATEGIES</span></div></div>
  <div class="hr-frame solid" style="left:419px"><div class="hr-box dark"><svg width="32" height="32" viewBox="0 0 32 32" fill="none" stroke="#fff" stroke-width="2"><rect x="7" y="4" width="18" height="22"/><path d="M11 11 H21 M11 16 H21 M11 21 H17"/></svg><span>STAFF ENGAGEMENT<br>SURVEY</span></div></div>
  <div class="hr-frame accentdash" style="left:670px"><div class="hr-box alt"><svg width="32" height="32" viewBox="0 0 32 32" fill="none" stroke="#fff" stroke-width="2"><circle cx="16" cy="10" r="5"/><path d="M6 28 C6 20 26 20 26 28"/></svg><span>STAFF ENGAGEMENT<br>PROGRAM</span></div></div>
  <ul class="list hr-list soft" style="left:188px"><li>New and relevant organizational structure</li><li>Updated roles and responsibilities</li><li>Inspiring objectives</li><li>Shared KPIs</li><li>Talent retention programs</li></ul>
  <ul class="list hr-list" style="left:439px"><li>Assess employee satisfaction and address concerns</li><li>Evaluate areas of improvement</li><li>Understand communication gaps</li></ul>
  <ul class="list alt hr-list" style="left:690px"><li>Foster positive work environment</li><li>Enhance employee satisfaction</li><li>Improve communication and engagement</li><li>Increase employee productivity</li><li>Improve Retention</li></ul>
  <div class="footer-line"></div><div class="page-no">6</div>
</section>

</body>
</html>
```